Make an Awesome Graphic for a PPT

Attached is the specific content for the project. the X-factor of Adoption. It does not need a title just take the existing graphic an improve it. Attached is our company logo for color palette and the "ugly version". It should look modern and edge in terms of effect and font. Need it by Monday March 7th

```html
<!DOCTYPE html>
<html lang="en">
<head>
<meta charset="utf-8">
<title>The X-Factor of Adoption</title>
<link rel="stylesheet" href="https://fonts.googleapis.com/css2?family=Orbitron:wght@500;700&display=swap">
<style>
  :root {
    --canvas: #ffffff;
    --steel-dark: #848997;
    --steel-mid: #a4a8b3;
    --steel-light: #c0c1ca;
    --blue-deep: #183f95;
    --blue-bright: #0574c1;
    --label: #ffffff;
  }
  html, body {
    margin: 0;
    padding: 0;
    width: 1200px;
    height: 761px;
    overflow: hidden;
    background: var(--canvas);
  }
  .slide {
    position: relative;
    width: 1200px;
    height: 761px;
  }
  .adoption-graphic {
    position: absolute;
    inset: 0;
    width: 1200px;
    height: 761px;
  }
  .quad-label {
    font-family: "Orbitron", sans-serif;
    font-weight: 500;
    font-size: 29px;
    fill: var(--label);
    letter-spacing: 1px;
  }
  .core-label {
    font-family: "Orbitron", sans-serif;
    font-weight: 700;
    font-size: 50px;
    fill: var(--label);
    letter-spacing: 3px;
  }
  .brand {
    position: absolute;
    right: 38px;
    bottom: 44px;
    display: flex;
    align-items: center;
    gap: 9px;
    font-family: "Orbitron", sans-serif;
    font-weight: 700;
    font-size: 32px;
    color: var(--blue-bright);
    letter-spacing: 1px;
  }
  .brand-mark {
    width: 16px;
    height: 16px;
    background: var(--blue-bright);
  }
</style>
</head>
<body>
<main class="slide">
  <svg class="adoption-graphic" viewBox="0 0 1900 1205" aria-label="The X-factor of adoption diagram">
    <defs>
      <linearGradient id="steelGradient" gradientUnits="userSpaceOnUse" x1="0" y1="200" x2="0" y2="1003">
        <stop offset="0" stop-color="var(--steel-dark)"/>
        <stop offset="0.5" stop-color="var(--steel-light)"/>
        <stop offset="1" stop-color="var(--steel-dark)"/>
      </linearGradient>
      <linearGradient id="blueGradient" x1="0" y1="0" x2="1" y2="0">
        <stop offset="0" stop-color="var(--blue-deep)"/>
        <stop offset="1" stop-color="var(--blue-bright)"/>
      </linearGradient>
      <linearGradient id="arrowGradient" x1="0" y1="0" x2="0" y2="1">
        <stop offset="0" stop-color="var(--steel-dark)"/>
        <stop offset="1" stop-color="var(--steel-light)"/>
      </linearGradient>
    </defs>

    <g class="accent-blocks" fill="url(#blueGradient)">
      <polygon points="548,213 686,350 686,452 717,483 610,590 548,528"/>
      <polygon points="1293,615 1352,673 1352,990 1215,853 1215,752 1184,721"/>
    </g>

    <g class="x-weave">
      <polygon class="x-frame" fill="url(#steelGradient)"
        points="560,200 880,200 950,268 1020,200 1340,200 1205,338 1100,338 1062,378 1160,482 1091,551 950,650 993,753 1062,822 1100,866 1205,866 1340,1003 1020,1003 950,935 880,1003 560,1003 695,866 800,866 838,822 740,720 807,653 757,603 745,475 838,378 800,338 695,338"/>
      <polygon class="x-band" fill="var(--steel-light)"
        points="548,672 745,475 800,560 950,603 1101,561 1215,447 1215,348 1352,212 1352,535 1064,823 993,753 950,700 795,641 686,750 686,855 550,990"/>
    </g>

    <g class="adoption-core">
      <polygon points="950,410 1143,603 950,796 757,603" fill="url(#blueGradient)"
        stroke="url(#blueGradient)" stroke-width="22" stroke-linejoin="round"/>
      <polygon points="950,467 992,505 908,505" fill="url(#arrowGradient)"/>
      <polygon points="908,700 992,700 950,740" fill="url(#arrowGradient)"/>
      <text class="core-label" x="950" y="602" text-anchor="middle">ADOPTION</text>
      <text class="core-label" x="950" y="656" text-anchor="middle">ZONE</text>
    </g>

    <g class="quadrant-labels">
      <text class="quad-label" x="646" y="259">FARMER</text>
      <text class="quad-label" x="666" y="296">EXPERIENCE</text>
      <text class="quad-label" x="1037" y="259">INNOVATION</text>
      <text class="quad-label" x="1064" y="296">CONCEPT</text>
      <text class="quad-label" x="672" y="940">INNOVATION</text>
      <text class="quad-label" x="645" y="977">CONCEPT</text>
      <text class="quad-label" x="1076" y="940">FARMER</text>
      <text class="quad-label" x="1051" y="977">SENTIMENT</text>
    </g>
  </svg>

  <div class="brand">
    <span class="brand-mark"></span>
    <span class="brand-name">AGRONEX</span>
  </div>
</main>
</body>
</html>
```